Kindle Grove Wording For Logo & Business card

I have the logo, I just need the "kindle Grove" wording to go with it, and a business card design. The only thing on the business card is the website info. We provide nature connection experiences, and bolster these efforts through writing and host a platform for community around it.

I also have an idea of what it could look like (sketch), though I'm really not sure how it would come out. I am open to the best design and happy to consider original artwork. You can see what the site is about at KindleGrove.com.

Contact Information for Business Card

The only thing on the business card is the website info and the design. I will put other messaging on the back.

Website lettering (KindleGrove.com) in Montserrat

Logo Text

Kindle Grove (letters optional)

Font styles to use
Other font styles liked:
• montserrat

```html
<!DOCTYPE html>
<html lang="en">
<head>
<meta charset="utf-8">
<title>Kindle Grove — Business Card</title>
<link rel="stylesheet" href="https://fonts.googleapis.com/css2?family=Montserrat:wght@300;400;500&display=swap">
<style>
  :root {
    --stage: #2e2e2f;
    --purple: #4d2b6e;
    --orange: #e2772a;
    --ink-grey: #4a4a4a;
    --card-light: #f1f3f2;
    --card-mid: #dfe4e1;
    --card-shade: #cfd6d2;
  }
  * { box-sizing: border-box; margin: 0; padding: 0; }
  html, body {
    width: 1200px; height: 780px; overflow: hidden;
    background: var(--stage);
    font-family: "Montserrat", sans-serif;
  }
  .stage {
    width: 1200px; height: 780px;
    display: flex; align-items: center; justify-content: center; gap: 50px;
  }
  .card {
    position: relative;
    width: 540px; height: 310px;
    border-radius: 22px;
    overflow: hidden;
    box-shadow: 0 14px 30px rgba(0,0,0,.45);
  }
  .card__backdrop {
    position: absolute; inset: 0;
    background:
      radial-gradient(ellipse at 30% 70%, var(--card-light) 0%, transparent 55%),
      radial-gradient(ellipse at 75% 25%, var(--card-shade) 0%, transparent 60%),
      linear-gradient(160deg, var(--card-mid), var(--card-light) 50%, var(--card-shade));
  }
  .edge-band {
    position: absolute; top: 0; bottom: 0; width: 16px;
    display: flex; gap: 3px;
  }
  .edge-band::before { content: ""; width: 3px; background: var(--purple); }
  .edge-band::after  { content: ""; width: 9px; background: var(--purple); }
  .edge-band--right { right: 0; }
  .edge-band--left  { left: 0; flex-direction: row-reverse; }

  .brand {
    position: absolute; left: 0; top: 0; bottom: 0; width: 200px;
    display: flex; flex-direction: column; align-items: center; justify-content: center; gap: 18px;
  }
  .brand__disc {
    width: 118px; height: 118px; border-radius: 50%;
    background: var(--purple);
    border: 4px solid #fff;
    box-shadow: 0 2px 6px rgba(0,0,0,.25);
  }
  .brand__name {
    font-weight: 300; font-size: 17px; letter-spacing: .12em;
    text-transform: uppercase; color: var(--ink-grey);
  }
  .divider {
    position: absolute; top: 0; bottom: 0; left: 206px;
    display: flex; gap: 3px;
  }
  .divider::before { content: ""; width: 7px; background: var(--purple); }
  .divider::after  { content: ""; width: 2px; background: var(--purple); }

  .contact {
    position: absolute; top: 50%; transform: translateY(-50%);
  }
  .card--brand .contact { left: 246px; }
  .card--plain .contact { left: 58px; }
  .contact__name {
    font-weight: 500; font-size: 26px; letter-spacing: .1em;
    color: var(--purple); text-transform: uppercase; line-height: 1;
  }
  .contact__role {
    font-weight: 400; font-size: 14px; color: var(--ink-grey);
    margin: 5px 0 20px;
  }
  .contact__web {
    display: flex; align-items: center; gap: 12px;
    font-size: 15.5px; font-weight: 400; color: var(--purple);
  }
  .contact__icon { width: 22px; height: 22px; flex: none; }
</style>
</head>
<body>
<svg width="0" height="0" style="position:absolute" aria-hidden="true">
  <symbol id="icon-web" viewBox="0 0 24 24">
    <circle cx="12" cy="12" r="11" fill="#e2772a"/>
    <g fill="none" stroke="#fff" stroke-width="1.3">
      <ellipse cx="12" cy="12" rx="5" ry="10.5"/>
      <path d="M2 8.5h20M1.5 12h21M2 15.5h20M12 1.5v21"/>
    </g>
  </symbol>
</svg>

<main class="stage">
  <article class="card card--brand">
    <div class="card__backdrop" role="img" aria-label="Faded aerial photograph of a whitewater river with a raft"></div>
    <div class="brand">
      <div class="brand__disc"></div>
      <div class="brand__name">Kindle Grove</div>
    </div>
    <div class="divider"></div>
    <div class="contact">
      <h1 class="contact__name">Mara Ellison</h1>
      <p class="contact__role">Founder</p>
      <p class="contact__web"><svg class="contact__icon"><use href="#icon-web"/></svg>www.kindlegrove.com</p>
    </div>
    <div class="edge-band edge-band--right"></div>
  </article>

  <article class="card card--plain">
    <div class="card__backdrop" role="img" aria-label="Faded aerial photograph of a whitewater river with a raft"></div>
    <div class="edge-band edge-band--left"></div>
    <div class="contact">
      <h2 class="contact__name">Mara Ellison</h2>
      <p class="contact__role">Founder</p>
      <p class="contact__web"><svg class="contact__icon"><use href="#icon-web"/></svg>www.kindlegrove.com</p>
    </div>
    <div class="edge-band edge-band--right"></div>
  </article>
</main>
</body>
</html>
```